Update Business Card Design

I'm looking to update my business cards. Attached is a photo of the current design. I like the black side so that does not have to be update. The white side needs to be updated. I want the design to be modern and minimalistic.
I am a lawyer and my firm's website is www.brennoxlegalco.com (for reference).
My firm's logo has a horizontal version (which is on the black side of the card) and a vertical version (on the white side). I would prefer to keep the vertical version on the white side and horizontal version on the black side (the logo files are attached).

I am open to redesigning the black side also. I would like one side to have the horizontal logo and the other to have the vertical logo.

```html
<!DOCTYPE html>
<html lang="en">
<head>
<meta charset="utf-8">
<title>Brennox Legal Co. — Business Card</title>
<link rel="stylesheet" href="https://fonts.googleapis.com/css2?family=Cinzel:wght@400;700&family=Arimo:wght@400&display=swap">
<style>
  :root {
    --stage: #6b6b6b;
    --paper: #f4f4f4;
    --ink: #3a3a3a;
    --brand-blue: #10b2d9;
    --panel-grey: #4a4b4d;
    --card-black: #000000;
    --white: #ffffff;
  }
  * { margin: 0; padding: 0; box-sizing: border-box; }
  html, body { width: 1200px; height: 963px; overflow: hidden; }
  body { background: var(--stage); position: relative; }

  .card { position: absolute; width: 318px; height: 556px; overflow: hidden; }
  .card--front { left: 222px; top: 174px; background: var(--paper); }
  .card--back { left: 636px; top: 174px; background: var(--card-black); }

  .holder-name {
    position: absolute; left: 35px; top: 60px;
    font-family: "Cinzel", serif; font-weight: 700; font-size: 21px;
    color: var(--brand-blue); letter-spacing: 0.2px;
  }
  .holder-title {
    position: absolute; left: 35px; top: 88px;
    font-family: "Arimo", sans-serif; font-size: 14px; color: var(--ink);
  }

  .contact-list { position: absolute; left: 35px; top: 140px; list-style: none;
    font-family: "Arimo", sans-serif; font-size: 13px; color: #4a4a4a; line-height: 16.6px; }
  .contact-item { display: flex; align-items: flex-start; }
  .contact-item--address { margin-bottom: 10px; }
  .contact-icon { width: 12px; height: 12px; margin-top: 2px; margin-right: 7px; flex: none; }

  .brand-panel {
    position: absolute; left: 144px; top: 391px; width: 174px; height: 165px;
    background: var(--panel-grey); border-top-left-radius: 36px;
  }
  .brand-band {
    position: absolute; left: 0; top: 476px; width: 281px; height: 80px;
    background: var(--brand-blue); border-bottom-right-radius: 26px;
  }
  .brand-name {
    position: absolute; left: 36px; top: 488px;
    font-family: "Cinzel", serif; font-weight: 400; font-size: 22px;
    line-height: 27px; color: var(--white);
  }
  .brand-mark {
    position: absolute; left: 190px; top: 414px; width: 84px; height: 84px;
    border-radius: 50%; background: var(--white);
  }

  .back-brand, .back-web {
    position: absolute; white-space: nowrap;
    transform: translate(-50%, -50%) rotate(-90deg);
  }
  .back-brand {
    left: 161px; top: 211px;
    font-family: "Cinzel", serif; font-weight: 400; font-size: 34px;
    line-height: 40px; color: var(--brand-blue); text-align: left;
  }
  .back-mark {
    position: absolute; left: 123px; top: 344px; width: 76px; height: 76px;
    border-radius: 50%; background: var(--brand-blue);
  }
  .back-web {
    left: 245px; top: 278px;
    font-family: "Cinzel", serif; font-weight: 700; font-size: 13px;
    letter-spacing: 3px; color: var(--white);
  }
</style>
</head>
<body>

<section class="card card--front" aria-label="Business card front">
  <h1 class="holder-name">DARIEN MOLTKE</h1>
  <p class="holder-title">Attorney at Law</p>

  <ul class="contact-list">
    <li class="contact-item contact-item--address">
      <svg class="contact-icon" viewBox="0 0 12 12" aria-hidden="true"><path d="M6 0.5a4 4 0 0 0-4 4c0 3 4 7 4 7s4-4 4-7a4 4 0 0 0-4-4z" fill="#10b2d9"/><circle cx="6" cy="4.5" r="1.5" fill="#f4f4f4"/></svg>
      <span>518 Larkmoor Avenue, Suite 312<br>Westvale, CA 90455</span>
    </li>
    <li class="contact-item">
      <svg class="contact-icon" viewBox="0 0 12 12" aria-hidden="true"><path d="M2.5 1l2 2.2-1 1.3a7 7 0 0 0 4 4l1.3-1 2.2 2-1.2 1.5C5 10.5 1.5 7 1 2.2z" fill="#10b2d9"/></svg>
      <span>555.204.3186</span>
    </li>
    <li class="contact-item">
      <svg class="contact-icon" viewBox="0 0 12 12" aria-hidden="true"><rect x="3" y="0.5" width="6" height="11" rx="1" fill="none" stroke="#10b2d9" stroke-width="1.3"/><circle cx="6" cy="9.6" r="0.7" fill="#10b2d9"/></svg>
      <span>555.317.6420</span>
    </li>
    <li class="contact-item">
      <svg class="contact-icon" viewBox="0 0 12 12" aria-hidden="true"><rect x="3" y="1" width="6" height="3" fill="#10b2d9"/><rect x="0.5" y="4.5" width="11" height="5" rx="1" fill="#10b2d9"/><rect x="3" y="8" width="6" height="3" fill="#f4f4f4" stroke="#10b2d9"/></svg>
      <span>555.204.3190</span>
    </li>
    <li class="contact-item">
      <svg class="contact-icon" viewBox="0 0 12 12" aria-hidden="true"><rect x="0.5" y="2.5" width="11" height="7" fill="#10b2d9"/><path d="M0.8 2.8L6 6.8l5.2-4" fill="none" stroke="#f4f4f4" stroke-width="1"/></svg>
      <span>darien@BrennoxLegalCo.com</span>
    </li>
    <li class="contact-item">
      <svg class="contact-icon" viewBox="0 0 12 12" aria-hidden="true"><circle cx="6" cy="6" r="5.5" fill="#10b2d9"/><path d="M3 3.5c1 0 1.5 1 2.5 1s0 2 1 2.5-1 2.5-1 2.5M8 2.5c0 1 1 1.5 2 1.5" fill="none" stroke="#f4f4f4" stroke-width="1"/></svg>
      <span>www.brennoxlegalco.com</span>
    </li>
  </ul>

  <div class="brand-panel" aria-hidden="true"></div>
  <div class="brand-band" aria-hidden="true"></div>
  <p class="brand-name">BRENNOX<br>LEGAL CO.</p>
  <div class="brand-mark" aria-hidden="true"></div>
</section>

<section class="card card--back" aria-label="Business card back">
  <p class="back-brand">BRENNOX<br>LEGAL CO.</p>
  <div class="back-mark" aria-hidden="true"></div>
  <p class="back-web">WWW.BRENNOXLEGALCO.COM</p>
</section>

</body>
</html>
```